Bramble Bunnies Business Cards

I need a business card for my new Company called Bramble Bunnies. We create handmade baby moccasins, headbands, t-shirts and more. I want some that will appeal to parents, and to go with the colors of my logo that I have attached. feel free to be creative. I would like my logo placed somewhere on the card.

Industry/Entity Type

Retail

Contact Information for Business Card

Bramble Bunnies
20418 Wexley C #5127
Irvine Ca 92687
Rosalind Hatchett Ceo
Info@Bramble-Bunnies.com
www.Bramble-Bunnies.com
Phone 9495817302

Requirements
Nice to have
• Logo included

```html
<!DOCTYPE html>
<html lang="en">
<head>
<meta charset="utf-8">
<title>Bramble Bunnies – Business Card</title>
<link rel="stylesheet" href="https://fonts.googleapis.com/css2?family=Itim&family=Arvo:wght@400;700&display=swap">
<style>
  :root {
    --backdrop: #d8d2c9;
    --card: #eef0ef;
    --card-edge: #dfe2e1;
    --ink: #1b1b1b;
    --orange: #d9773f;
    --night: #151515;
    --divider: #d3d6d5;
  }
  html, body {
    margin: 0;
    width: 1200px;
    height: 970px;
    overflow: hidden;
    background: var(--backdrop);
  }
  .card {
    position: absolute;
    left: 110px;
    top: 212px;
    width: 980px;
    height: 545px;
    background: var(--card);
    border: 1px solid var(--card-edge);
    box-shadow: 0 18px 40px rgba(0,0,0,.18);
    overflow: hidden;
  }
  .divider {
    position: absolute;
    left: 472px;
    top: 0;
    width: 1px;
    height: 473px;
    background: var(--divider);
  }
  .brand {
    position: absolute;
    left: 0;
    width: 472px;
    top: 215px;
    display: flex;
    align-items: center;
    justify-content: center;
    gap: 16px;
  }
  .brand-square {
    width: 30px;
    height: 30px;
    background: var(--orange);
  }
  .brand-name {
    font-family: "Itim", cursive;
    font-size: 52px;
    color: var(--ink);
    white-space: nowrap;
  }
  .person-name {
    position: absolute;
    left: 512px;
    top: 70px;
    margin: 0;
    font-family: "Itim", cursive;
    font-size: 36px;
    font-weight: 400;
    letter-spacing: .5px;
    color: var(--ink);
  }
  .person-role {
    position: absolute;
    left: 512px;
    top: 124px;
    font-family: "Arvo", serif;
    font-weight: 700;
    font-size: 17px;
    color: var(--ink);
  }
  .contact {
    position: absolute;
    left: 516px;
    font-family: "Arvo", serif;
    font-size: 21px;
    color: var(--ink);
    display: flex;
    align-items: center;
    gap: 16px;
  }
  .contact svg { width: 22px; height: 18px; fill: var(--orange); }
  .contact-phone { top: 236px; }
  .contact-email { top: 273px; }
  .address {
    position: absolute;
    left: 512px;
    top: 326px;
    font-family: "Arvo", serif;
    font-size: 21px;
    line-height: 35px;
    letter-spacing: .5px;
    color: var(--ink);
  }
  .footer-bands {
    position: absolute;
    left: 0;
    bottom: 0;
    width: 980px;
    height: 72px;
  }
  .website {
    position: absolute;
    left: 489px;
    right: 0;
    bottom: 0;
    height: 72px;
    display: flex;
    align-items: center;
    padding-left: 38px;
    font-family: "Arvo", serif;
    font-weight: 700;
    font-size: 20px;
    color: var(--orange);
    letter-spacing: .3px;
  }
</style>
</head>
<body>
  <div class="card">
    <div class="divider"></div>

    <div class="brand">
      <div class="brand-square"></div>
      <div class="brand-name">Bramble Bunnies</div>
    </div>

    <h1 class="person-name">Rosalind Hatchett</h1>
    <div class="person-role">CEO</div>

    <div class="contact contact-phone">
      <svg viewBox="0 0 22 18" aria-hidden="true">
        <path d="M1 6 Q11 -1 21 6 L19 9 L15 7 L15 5 Q11 3 7 5 L7 7 L3 9 Z"/>
        <path d="M6 9 L16 9 L19 17 L3 17 Z"/>
      </svg>
      <span>9495817302</span>
    </div>
    <div class="contact contact-email">
      <svg viewBox="0 0 22 18" aria-hidden="true">
        <path d="M1 3 H21 V16 H1 Z M2.5 4.5 L11 11 L19.5 4.5" fill="var(--orange)" stroke="var(--card)" stroke-width="1.4"/>
      </svg>
      <span>Info@Bramble-Bunnies.com</span>
    </div>

    <div class="address">20418 Wexley C<br>#5127 Irvine CA 92687</div>

    <svg class="footer-bands" viewBox="0 0 980 72" aria-hidden="true">
      <rect x="0" y="36" width="472" height="36" fill="var(--orange)"/>
      <polygon points="489,0 980,0 980,72 443,72" fill="var(--night)"/>
    </svg>
    <div class="website">www.Bramble-Bunnies.com</div>
  </div>
</body>
</html>
```